Kestrelmoor business card

We're looking to "refresh" our original Kestrelmoor logo design and also get a new business card design. We're a modern consulting and software business that's been around 4-years now. We work with large professional companies and therefore require a design that is simple and professional. We would like to retain the notch in the "A" and just the word "Kestrelmoor" as the logo. We like greys, silvers, black, white...but happy to explore highlight color. We're looking for understated modern.

Industry/Entity Type

Software

```html
<!DOCTYPE html>
<html lang="en">
<head>
<meta charset="utf-8">
<title>Kestrelmoor business card</title>
<link rel="stylesheet" href="https://fonts.googleapis.com/css2?family=Barlow:wght@500&display=swap">
<style>
  :root {
    --backdrop: #849ba9;
    --card-light: #e7e7e7;
    --card-dark: #424f59;
    --ink-dark: #414f5a;
    --ink-light: #ffffff;
    --accent: #8aa3b0;
  }
  * { margin: 0; padding: 0; box-sizing: border-box; }
  html, body {
    width: 1200px;
    height: 1000px;
    overflow: hidden;
    background: var(--backdrop);
    font-family: "Barlow", sans-serif;
  }
  .card {
    position: absolute;
    width: 630px;
    height: 360px;
  }
  .card-front {
    left: 97px;
    top: 94px;
    background: var(--card-light);
    display: flex;
    align-items: center;
    justify-content: center;
  }
  .wordmark {
    font-weight: 500;
    font-size: 72px;
    letter-spacing: -0.5px;
    color: var(--ink-dark);
    line-height: 1;
  }
  .card-back {
    left: 443px;
    top: 516px;
    background: var(--card-dark);
    color: var(--ink-light);
    font-weight: 500;
  }
  .accent-square {
    position: absolute;
    right: 50px;
    top: 30px;
    width: 60px;
    height: 60px;
    background: var(--accent);
  }
  .contact {
    position: absolute;
    left: 51px;
    top: 88px;
  }
  .contact-name { font-size: 22px; line-height: 34px; }
  .contact-title { font-size: 20px; line-height: 34px; margin-bottom: 34px; }
  .contact-line { font-size: 18px; line-height: 32px; }
</style>
</head>
<body>
  <section class="card card-front">
    <span class="wordmark">Kestrelmoor</span>
  </section>

  <section class="card card-back">
    <div class="accent-square"></div>
    <div class="contact">
      <p class="contact-name">Your Name</p>
      <p class="contact-title">Title</p>
      <p class="contact-line">Address Line 1</p>
      <p class="contact-line">Address Line 1</p>
      <p class="contact-line">Tel: 0123456789&nbsp; Fax: 0123456789</p>
      <p class="contact-line">mail@website.com&nbsp; www.website.com</p>
    </div>
  </section>
</body>
</html>
```